Task Description:
I’m wanting a professionally designed 8 ½' x 11, 3 fold brochure, both sides, to print as my target audience are those people who primarily don’t have access to the internet. These items will be dropped off in the mailboxes of all households in the city.
However I do have a web site www.civicharborvote.ca where I would like to have it as a document that can be down loaded.
This is my first foray into political office and my message needs to be clear, concise and easy to understand. The brochure should be a bit conservative yet be warm and inviting. I’ve selected two pictures that I think make sense under their respective headings, but I'm open to suggestions.I need to update my picture for the front cover.
There is the possibility of having T shirts and business cards made up, which would be in essence a simpler version of the brochure so please keep this in mind. I ask that you work with me and I will compensate you accordingly for the extras should they be required. You may want to consider making the Civic Harbor Vote into a logo as we own all the web extensions and have applied for copyright protection for branding purposes.
You may want to look at QL Brightmoor http://www.qlbrightmoor.ca/ , or the Silver Pine Trust of Canada www.silverpinetrust.com as two recognizable colour schemes here in Canada but don’t let that limit your imagination.
The content in the flier should remain intact although I am open to some minor suggestions. As you can see my talents as a graphic artist are limited hence my need for that professional make over that will give it a bit of razzle dazzle and set me out from the other candidates. So use your imagination!!
Target Market(s)
Middle age voters who may or may not have access to the internet and still prefer print
Industry/Entity Type
Conservative
Look and feel

```html
<!DOCTYPE html>
<html lang="en">
<head>
<meta charset="utf-8">
<title>Dean Marlow – Civic Harbor Vote brochure</title>
<link href="https://fonts.googleapis.com/css2?family=Signika:wght@300;400;600;700&display=swap" rel="stylesheet">
<style>
:root{
  --bg-dark:#1a0d08;
  --bg-mid:#3a1a10;
  --bg-warm:#5a2616;
  --ink-white:#ffffff;
  --ink-body:#c9bdb2;
  --ink-stone:#b7aca2;
  --rule:#8d7f75;
  --footer-top:#e2dfdc;
  --footer-bottom:#b9b5b1;
  --footer-ink:#8a837d;
  --footer-strong:#6e6761;
}
*{margin:0;padding:0;box-sizing:border-box}
html,body{width:1200px;height:848px;overflow:hidden;background:var(--bg-dark)}
body{font-family:"Signika",sans-serif;color:var(--ink-body)}
.brochure{position:relative;width:1200px;height:848px;overflow:hidden;
  background:
    radial-gradient(ellipse 420px 520px at 1000px 300px,rgba(150,40,20,.55),transparent 70%),
    radial-gradient(ellipse 700px 400px at 300px 300px,rgba(90,40,25,.35),transparent 70%),
    linear-gradient(180deg,var(--bg-mid) 0%,var(--bg-dark) 45%,var(--bg-warm) 100%);}
.top-rule{position:absolute;left:0;top:20px;width:1200px;height:1px;background:var(--rule);opacity:.6}
.panel{position:absolute;top:0;height:797px}
.panel--left{left:0;width:400px}
.panel--middle{left:400px;width:400px}
.panel--cover{left:800px;width:400px}
.abs{position:absolute}
.heading-small{font-weight:700;color:var(--ink-white);font-size:32px;letter-spacing:-1px;line-height:1}
.heading-light{font-weight:400;color:var(--ink-white);font-size:37px;letter-spacing:-.5px;line-height:1}
.stone{color:var(--ink-stone);font-weight:700}
.body-text{font-weight:300;font-size:14.2px;line-height:21px;color:var(--ink-body)}
.body-text strong{color:var(--ink-white);font-weight:600}
.intro-name{font-size:22px;font-weight:600;color:var(--ink-white);letter-spacing:-.5px}
.intro-name .stone{font-size:22px}
.intro-name-tail{font-size:14px;font-weight:400;color:var(--ink-white)}
.family-list{list-style:none}
.family-list li{font-weight:300;font-size:14.2px;line-height:22px;color:var(--ink-white);padding-left:12px;position:relative;margin-bottom:13px}
.family-list li::before{content:"•";position:absolute;left:2px;color:var(--ink-stone)}
.quote-mark{font-weight:700;color:var(--ink-stone);font-size:110px;line-height:1}
.involved-heading{font-weight:700;color:var(--ink-white);font-size:42px;letter-spacing:-1.5px;line-height:44px}
.photo{border:1px solid #d8d0c8}
.photo-caption{position:absolute;left:0;bottom:0;background:rgba(0,0,0,.75);color:#fff;font-size:11px;padding:3px 8px;font-weight:400}
.vote-block{text-align:center;color:var(--ink-white)}
.vote-date{font-size:25px;font-weight:400;letter-spacing:-.5px}
.vote-date b{font-weight:700}
.vote-name{font-size:48px;font-weight:700;line-height:44px;letter-spacing:-1.5px}
.vote-name small{font-size:26px;font-weight:600}
.vote-surname{font-size:60px;font-weight:700;color:var(--ink-stone);line-height:56px;letter-spacing:-2px}
.cover-title{color:var(--ink-white);font-weight:700;font-size:41px;line-height:45px;letter-spacing:-1.5px}
.cover-title .thin{font-weight:300;font-size:30px;letter-spacing:-.5px}
.cover-title .mid{font-size:32px}
.cover-rule{position:absolute;left:8px;top:526px;width:392px;height:1px;background:var(--rule)}
.candidate-first{font-size:60px;font-weight:400;color:var(--ink-white);letter-spacing:-2px;line-height:58px}
.candidate-last{font-size:62px;font-weight:700;color:var(--ink-stone);letter-spacing:-2px;line-height:60px}
.tagline{font-size:34px;font-weight:400;color:var(--ink-white);letter-spacing:-1px}
.tagline .stone{font-weight:700}
.divider-dot{width:8px;height:8px;background:var(--ink-stone);transform:rotate(45deg);opacity:.7}
.footer{position:absolute;left:0;top:797px;width:1200px;height:51px;background:linear-gradient(180deg,var(--footer-top),var(--footer-bottom));display:flex}
.footer-url{width:400px;text-align:center;line-height:47px;font-size:22px;font-weight:400;color:var(--footer-ink);letter-spacing:-.3px}
.footer-url b{color:var(--footer-strong);font-weight:700}
</style>
</head>
<body>
<div class="brochure">
  <div class="top-rule"></div>

  <section class="panel panel--left">
    <div class="abs" style="left:40px;top:48px">
      <div class="heading-small">Getting to know...</div>
      <div class="heading-light" style="margin-top:8px">Civic Harbor <span class="stone">Vote</span></div>
    </div>
    <p class="abs body-text" style="left:40px;top:170px;width:330px">
      <span class="intro-name">Dean <span class="stone">Marlow</span></span>
      <span class="intro-name-tail"> is a life long resident of Harbor Falls.</span><br>
      My family has served this community and area for more than 100 years.
    </p>
    <ul class="abs family-list" style="left:56px;top:263px;width:320px">
      <li>Walter James Marlow built and managed the Lakeside Elevator.</li>
      <li>Frank Ellis Marlow managed the Granite Bay Cement facility</li>
      <li>Ruth Anne Marlow was past president of the Chamber of Commerce.</li>
      <li>Jenna Marlow is a gold medalist at the 2010 Winter Olympics.</li>
    </ul>
    <p class="abs body-text" style="left:40px;top:500px;width:334px;text-align:justify">
      Although I have a unique vocation through the Quality Assurance Guild (QAG) and could live and work anywhere in the world I have chosen to remain and work from Harbor Falls.
    </p>
    <p class="abs body-text" style="left:40px;top:628px;width:334px;text-align:justify">
      On average I visit and work with more than 30 different corporations a year. I have a high pressure job as companies rely on my skills and expertise to keep them safe and operational. Solving problems, minimizing costs, maximizing production are challenges I face everyday.
    </p>
  </section>

  <section class="panel panel--middle">
    <div class="abs quote-mark" style="left:24px;top:16px">“</div>
    <h2 class="abs involved-heading" style="left:84px;top:38px">I’m currently<br><span style="margin-left:-54px">involved with...</span></h2>
    <p class="abs body-text" style="left:30px;top:148px;width:338px">
      <strong>Voltaris Labs Inc.</strong> a newly created R&amp;D company developing electric propulsion systems for the transit industry. Our research partners consist of faculty and students from Northshore University. So I know first hand how difficult it is to start, finance and run a new business in this city.
    </p>
    <div class="abs photo" role="img" aria-label="Photo of the candidate's father at age 92 seated in an arena beside the university mascot" style="left:27px;top:285px;width:325px;height:154px;background:linear-gradient(135deg,#6d655e 0%,#9c958f 45%,#b9b3ad 70%,#6a5048 100%)">
      <span class="photo-caption">My Dad @ 92 with NSU Mascot</span>
    </div>
    <p class="abs body-text" style="left:30px;top:458px;width:338px;text-align:justify">
      As <strong>Civic Harbor <span class="stone">Vote</span></strong>, my goal is to be mayor for two terms, maximum three. With the implementation of a long term plan we will require a fresh face to step forward to complete the process. I also feel that we should reduce the number of city councilors and use those funds to make those positions full time. Term limits should apply to all elected positions!
    </p>
    <div class="abs quote-mark" style="left:292px;top:580px">”</div>
    <div class="abs vote-block" style="left:80px;top:628px;width:230px">
      <div class="vote-date">On <b>Oct 25th</b></div>
      <div class="vote-name"><small>Vote:</small> Dean</div>
      <div class="vote-surname">Marlow</div>
    </div>
  </section>

  <section class="panel panel--cover">
    <div class="abs" role="img" aria-label="Photo of a hand holding an ornate brass key with a small house on its bit" style="left:8px;top:0;width:392px;height:526px;background:radial-gradient(ellipse 200px 260px at 210px 310px,rgba(200,150,60,.55),rgba(120,50,20,.35) 55%,transparent 80%)"></div>
    <h1 class="abs cover-title" style="left:27px;top:38px;width:360px">
      Unlock <span class="thin">the</span> Potential<br>
      <span class="thin">of the</span> Best <span class="mid">Small</span><br>
      City <span class="thin">in</span><br>
      North<br>
      America
    </h1>
    <div class="cover-rule"></div>
    <div class="abs" role="img" aria-label="Head and shoulders portrait of the candidate" style="left:53px;top:545px;width:110px;height:127px;background:linear-gradient(180deg,#d9d9d9,#a9a9a9);border:2px solid #fff"></div>
    <div class="abs" style="left:172px;top:548px">
      <div class="candidate-first">Dean</div>
      <div class="candidate-last">Marlow</div>
    </div>
    <div class="abs divider-dot" style="left:196px;top:702px"></div>
    <div class="abs tagline" style="left:0;top:727px;width:400px;text-align:center">Civic Harbor <span class="stone">Vote</span></div>
  </section>

  <footer class="footer">
    <div class="footer-url">www.civicharbor<b>vote</b>.ca</div>
    <div class="footer-url">www.civicharbor<b>vote</b>.ca</div>
    <div class="footer-url">www.civicharbor<b>vote</b>.ca</div>
  </footer>
</div>
</body>
</html>
```